KV MOTORS BANNER/SIGN DESIGN

Design a banner sign for outdoor use for KV MOTORS - a premium pre owned vehicle sales center. The size must be 36 feet in width
and 3 feet in height.

Information required: logo (attached)
-PREMIUM PRE-OWEND VEHICLE SALES
- 403.555.0172

perhaps in smaller font: BUY-SELL-TRADE

prefer white background but could possibly do red matching the logo

```html
<!DOCTYPE html>
<html lang="en">
<head>
<meta charset="utf-8">
<title>KV Motors Banner</title>
<link href="https://fonts.googleapis.com/css2?family=Anton&display=swap" rel="stylesheet">
<style>
  :root {
    --backdrop: #808080;
    --brand-red: #e30613;
    --white: #ffffff;
    --black: #000000;
    --accent-yellow: #ffed00;
  }
  * { margin: 0; padding: 0; box-sizing: border-box; }
  html, body {
    width: 1200px;
    height: 600px;
    overflow: hidden;
    background: var(--backdrop);
    font-family: "Anton", "Arial Narrow", sans-serif;
  }
  .banner {
    position: absolute;
    left: 87px;
    top: 257px;
    width: 1026px;
    height: 86px;
    background: var(--brand-red);
    overflow: hidden;
    box-shadow: 0 6px 14px rgba(0,0,0,0.35);
  }
  .brand-panel {
    position: absolute;
    inset: 0;
  }
  .brand-panel svg { display: block; }
  .brand-name {
    position: absolute;
    left: 22px;
    top: 24px;
    display: flex;
    align-items: center;
    gap: 10px;
  }
  .brand-dot {
    width: 38px;
    height: 38px;
    border-radius: 50%;
    background: var(--brand-red);
  }
  .brand-text {
    font-size: 24px;
    line-height: 1;
    color: var(--black);
    letter-spacing: 1.5px;
  }
  .headline {
    position: absolute;
    left: 218px;
    top: 18px;
    font-size: 54px;
    font-weight: 400;
    line-height: 1;
    color: var(--white);
    white-space: nowrap;
    transform: scaleX(0.83);
    transform-origin: left top;
    text-shadow:
      1px 2px 0 var(--black), 2px 3px 0 var(--black), 3px 4px 0 var(--black),
      4px 6px 0 var(--black), 5px 7px 0 var(--black), 6px 8px 0 var(--black),
      7px 10px 0 var(--black), 8px 11px 0 var(--black), 9px 12px 0 var(--black),
      10px 14px 0 var(--black), 11px 15px 0 var(--black), 12px 16px 0 var(--black),
      13px 18px 0 var(--black), 14px 19px 0 var(--black), 15px 20px 0 var(--black),
      16px 22px 0 var(--black), 17px 23px 0 var(--black), 18px 24px 0 var(--black),
      19px 26px 0 var(--black), 20px 27px 0 var(--black), 21px 28px 0 var(--black),
      22px 30px 0 var(--black), 23px 31px 0 var(--black), 24px 32px 0 var(--black);
  }
  .contact {
    position: absolute;
    left: 852px;
    top: 0;
    width: 150px;
    height: 86px;
  }
  .services {
    position: absolute;
    left: -20px;
    right: -20px;
    top: 14px;
    text-align: center;
    font-size: 27px;
    line-height: 1;
    color: var(--accent-yellow);
    white-space: nowrap;
    transform: scaleX(0.8);
  }
  .phone {
    position: absolute;
    left: 0;
    top: 45px;
    width: 150px;
    height: 26px;
    border-radius: 13px;
    background: var(--black);
    color: var(--white);
    text-align: center;
    font-size: 21px;
    line-height: 26px;
    white-space: nowrap;
  }
</style>
</head>
<body>
  <div class="banner">
    <div class="brand-panel">
      <svg width="1026" height="86" viewBox="0 0 1026 86" aria-hidden="true">
        <polygon points="0,0 188,0 214,86 0,86" fill="#ffffff"/>
      </svg>
      <div class="brand-name">
        <span class="brand-dot"></span>
        <span class="brand-text">KV MOTORS</span>
      </div>
    </div>
    <h1 class="headline">PREMIUM PRE-OWEND VEHICLE SALES</h1>
    <div class="contact">
      <p class="services">BUY-SELL-TRADE</p>
      <p class="phone">403.555.0172</p>
    </div>
  </div>
</body>
</html>
```